Business Card Design

I would like a new business card design for an accounting firm that specializes in resolving clients tax problems. I want the card to give the impression that we are not your typical stodgy accounting firm, but at the same time we will get the job done.
Industry/Entity Type
Business
Contact Information for Business Card
Dorian T Welsby
Certified Public Accountant
38-27 52nd Street
Sunnyside, NY 11287
Tel: (718) 555-0142
Fax: (888) 555-0199
e-mail: dtwthecpa@ledgerpost.com
website: harborfilingreliefexperts.com

```html
<!DOCTYPE html>
<html lang="en">
<head>
<meta charset="utf-8">
<title>Dorian T Welsby – Business Card</title>
<link rel="stylesheet" href="https://fonts.googleapis.com/css2?family=Ubuntu:wght@400;500;700&display=swap">
<style>
  :root {
    --backdrop: #f3a9a6;
    --card: #f6f7f7;
    --slate: #36474f;
    --green: #8cbb3e;
    --text: #4a5a61;
  }
  * { margin: 0; padding: 0; box-sizing: border-box; }
  html, body { width: 1200px; height: 1080px; overflow: hidden; }
  body {
    background: var(--backdrop);
    font-family: "Ubuntu", sans-serif;
    position: relative;
  }
  .card {
    position: absolute;
    left: 100px; top: 254px;
    width: 1000px; height: 572px;
    background: var(--card);
    box-shadow: 0 18px 40px rgba(120, 40, 40, 0.25);
    overflow: hidden;
  }
  .edge-band {
    position: absolute; top: 0; height: 12px;
    background: var(--slate);
  }
  .edge-band--left { left: 0; width: 440px; }
  .edge-band--right { right: 0; width: 110px; }
  .brand {
    position: absolute;
    left: 0; top: 0; width: 470px; height: 572px;
    display: flex; flex-direction: column;
    align-items: center; justify-content: center; gap: 26px;
  }
  .brand__square {
    width: 110px; height: 110px;
    background: var(--slate);
  }
  .brand__name {
    font-weight: 700; font-size: 52px; letter-spacing: 2px;
    color: var(--slate);
  }
  .divider {
    position: absolute; left: 480px; top: 150px;
    width: 2px; height: 280px;
    background: var(--green);
  }
  .contact {
    position: absolute; left: 520px; top: 150px; width: 440px;
    color: var(--text);
  }
  .contact__name {
    font-weight: 700; font-size: 44px; color: var(--slate);
    line-height: 1.1;
  }
  .contact__rule {
    height: 3px; width: 100%;
    background: var(--green);
    margin: 8px 0 10px;
  }
  .contact__title {
    font-size: 19px; font-weight: 500; color: var(--slate);
    text-align: right; margin-bottom: 6px;
  }
  .contact__address {
    font-size: 17px; text-align: right; margin-bottom: 18px;
  }
  .contact__list { list-style: none; }
  .contact__item {
    display: flex; align-items: center; gap: 12px;
    font-size: 17px; margin-bottom: 10px;
  }
  .contact__icon { width: 24px; height: 24px; flex: none; }
</style>
</head>
<body>
  <main class="card">
    <div class="edge-band edge-band--left"></div>
    <div class="edge-band edge-band--right"></div>

    <section class="brand">
      <div class="brand__square"></div>
      <div class="brand__name">LOGO HERE</div>
    </section>

    <div class="divider"></div>

    <section class="contact">
      <h1 class="contact__name">Dorian T Welsby</h1>
      <div class="contact__rule"></div>
      <p class="contact__title">Certified Public Accountant</p>
      <p class="contact__address">38-27 52nd Street Sunnyside, NY 11287</p>
      <ul class="contact__list">
        <li class="contact__item">
          <svg class="contact__icon" viewBox="0 0 24 24"><circle cx="12" cy="12" r="12" fill="var(--green)"/><path d="M8 6.5l2 .2 1 2.8-1.4 1.1a8 8 0 0 0 3.8 3.8l1.1-1.4 2.8 1 .2 2c-.2.8-1 1.3-1.8 1.2A11 11 0 0 1 6.8 8.3c-.1-.8.4-1.6 1.2-1.8z" fill="#fff"/></svg>
          Tel: (718) 555-0142
        </li>
        <li class="contact__item">
          <svg class="contact__icon" viewBox="0 0 24 24"><circle cx="12" cy="12" r="12" fill="var(--green)"/><rect x="8" y="5.5" width="8" height="4" fill="#fff"/><rect x="6" y="10" width="12" height="6" rx="1" fill="#fff"/><rect x="8.5" y="14" width="7" height="4.5" fill="#fff" stroke="var(--green)" stroke-width="1"/></svg>
          Fax: (888) 555-0199
        </li>
        <li class="contact__item">
          <svg class="contact__icon" viewBox="0 0 24 24"><circle cx="12" cy="12" r="12" fill="var(--green)"/><rect x="6" y="8" width="12" height="8.5" rx="1" fill="#fff"/><path d="M6.5 8.5l5.5 4.5 5.5-4.5" fill="none" stroke="var(--green)" stroke-width="1.2"/></svg>
          dtwthecpa@ledgerpost.com
        </li>
        <li class="contact__item">
          <svg class="contact__icon" viewBox="0 0 24 24"><circle cx="12" cy="12" r="12" fill="var(--green)"/><circle cx="12" cy="12" r="6" fill="none" stroke="#fff" stroke-width="1.4"/><ellipse cx="12" cy="12" rx="2.6" ry="6" fill="none" stroke="#fff" stroke-width="1.2"/><path d="M6 12h12" stroke="#fff" stroke-width="1.2"/></svg>
          harborfilingreliefexperts.com
        </li>
      </ul>
    </section>
  </main>
</body>
</html>
```